CALMIVERA BROCHURE/CATALOG DESIGN
SPA AND WELLNESS CENTRE
We need a new design for our brochure/catalogue. This is related to spa industry. We have over 10 locations and expanding. We need the design to be modern and must resemble some parts of our logo design as well.
for services and price list:
http://www.calmiverahealth.example/services_massage.php
For locations:
http://www.calmiverahealth.example/locations.php
Must say somewhere in services and prices:
1) Please speak to our receptionist for any insurance related questions. (or something similar)
2) Gift Certificates Available and redeemable at any of our locations.
3) Package Card Available and usable at any of our locations.
#2 and #3 can be used in a paragraph form in our about us section.
Also please include out website:
www.calmiverahealth.example
Salon & Spa
Corporate/family/fun/personal/wellness/female/male/any age
Must be modern!
Must resemble the spa/wellness industry type design!
Must have all our services and prices!
Must be easy to read our services and prices!
We suggest the brochure to have following:
About Calmivera
Services and Prices
Locations
We think in order to fit all servies and prices and about us info, may be ok to use 4 page layout for brochure design.

```html
<!DOCTYPE html>
<html lang="en">
<head>
<meta charset="utf-8">
<title>Calmivera Brochure</title>
<link rel="stylesheet" href="https://fonts.googleapis.com/css2?family=Open+Sans:ital,wght@0,400;0,600;0,700;0,800;1,400&display=swap">
<style>
  :root {
    --blue: #1c72b8;
    --blue-dark: #0d4d8a;
    --blue-light: #4fa3dc;
    --lime: #9bc31c;
    --lime-dark: #7ea312;
    --ink: #3d4650;
    --paper: #ffffff;
    --backdrop: #e9eaec;
  }
  * { box-sizing: border-box; margin: 0; padding: 0; }
  html, body { width: 1200px; height: 927px; overflow: hidden; }
  body {
    background: var(--backdrop);
    font-family: "Open Sans", Arial, sans-serif;
    color: var(--ink);
  }
  .brochure {
    position: absolute;
    left: 50px; top: 38px;
    width: 1100px; height: 850px;
    background: var(--paper);
    display: flex;
    box-shadow: 0 4px 18px rgba(0,0,0,.12);
    overflow: hidden;
  }
  .bands { position: absolute; inset: 0; pointer-events: none; }
  .panel {
    position: relative;
    width: 366.67px;
    height: 100%;
    padding: 96px 30px 120px;
    border-right: 1px solid #eef0f2;
  }
  .panel:last-child { border-right: 0; }
  .panel-title {
    position: absolute; top: 26px; left: 30px;
    color: #fff; font-weight: 800; font-size: 20px; letter-spacing: 1px;
  }
  .site-url {
    position: absolute; top: 28px; right: 30px;
    color: #fff; font-weight: 600; font-size: 13px;
  }
  h2 {
    color: var(--lime-dark);
    font-size: 16px; font-weight: 700;
    margin: 0 0 6px;
  }
  p, li { font-size: 11.5px; line-height: 1.6; }
  .section { margin-bottom: 20px; }
  .notices { padding-left: 18px; }
  .notices li { margin-bottom: 6px; }
  .photo {
    position: absolute;
    border-radius: 14px;
  }
  .photo-hands {
    left: 30px; bottom: 132px; width: 170px; height: 120px;
    background: linear-gradient(135deg, #f2d2c0, #d9a589 60%, #b97c62);
    border-radius: 60px 14px 14px 14px;
  }
  .photo-woman {
    right: 0; top: 330px; width: 150px; height: 250px;
    background: linear-gradient(160deg, #f4e8de, #d7ab8c 55%, #8a5a42);
    border-radius: 120px 0 0 120px;
  }
  .gift { padding-left: 185px; margin-top: -2px; }
  .gift p { font-size: 11px; }
  .special-band {
    background: var(--lime);
    color: #fff; font-weight: 800; font-size: 14px; letter-spacing: 1px;
    padding: 6px 12px; margin: 4px 0 14px;
    width: 190px;
  }
  .package { width: 170px; margin-bottom: 14px; }
  .package h3 { color: var(--blue); font-size: 14px; font-weight: 700; }
  .package ul { list-style: none; }
  .package li { font-size: 11px; line-height: 1.55; display: flex; gap: 6px; align-items: center; }
  .tick { width: 10px; height: 10px; flex: none; }
  .price { color: var(--lime-dark); font-weight: 800; font-size: 16px; }
  .footer-note {
    position: absolute; left: 0; right: 0; bottom: 24px;
    color: #fff; font-size: 12px; text-align: center; font-weight: 600;
  }
  .footer-note strong { display: block; font-size: 13px; margin-top: 4px; }
</style>
</head>
<body>
<div class="brochure">
  <svg class="bands" width="1100" height="850" viewBox="0 0 1100 850" aria-hidden="true">
    <path d="M0 0H1100V62C900 92 700 50 480 70C300 86 150 62 0 84Z" fill="var(--blue)"/>
    <path d="M0 84C150 62 300 86 480 70C700 50 900 92 1100 62V70C900 100 700 58 480 78C300 94 150 70 0 92Z" fill="var(--lime)"/>
    <path d="M0 850V760C200 730 420 790 640 760C820 736 960 770 1100 745V850Z" fill="var(--blue-dark)"/>
    <path d="M0 752C200 722 420 782 640 752C820 728 960 762 1100 737V745C960 770 820 736 640 760C420 790 200 730 0 760Z" fill="var(--lime)"/>
  </svg>

  <section class="panel about">
    <div class="panel-title">ABOUT US</div>
    <div class="section">
      <h2>What We Do</h2>
      <p>At Calmivera we bring calm to busy lives. Our therapists offer massage, facials, body care and wellness treatments for every age in a warm and quiet setting across more than ten locations.</p>
    </div>
    <div class="section">
      <h2>Upon Arrival</h2>
      <p>Please arrive ten minutes before your appointment to fill in a short health form. Our staff will welcome you, offer a warm drink and guide you to a private room where your treatment begins.</p>
    </div>
    <div class="section gift">
      <h2>Gift Certificates</h2>
      <p>Gift Certificates are available and redeemable at any of our locations. Package Cards are also available and usable at any of our locations, making it easy to share calm with friends and family.</p>
    </div>
    <div class="photo photo-hands" role="img" aria-label="Photo of a therapist's hands giving a back massage"></div>
  </section>

  <section class="panel info">
    <div class="section">
      <h2>Reservations</h2>
      <p>We recommend booking ahead to secure your preferred time and therapist. Call any location or book online. Please give us 24 hours notice to change or cancel.</p>
    </div>
    <div class="section">
      <h2>Groups</h2>
      <p>Planning a spa day for a team, a party or a family? Ask about our group rates and private bookings for four or more guests.</p>
    </div>
    <div class="section">
      <h2>Other Important Notices</h2>
      <ol class="notices">
        <li>Please speak to our receptionist for any insurance related questions.</li>
        <li>Late arrivals may shorten your treatment time.</li>
        <li>Please keep phones on silent in treatment areas.</li>
        <li>Tell your therapist about any health concerns before starting.</li>
        <li>Gratuities are at your discretion.</li>
      </ol>
    </div>
    <div class="footer-note">Showers, lounges and change rooms available at all locations.<strong>Visit us online to find the spa nearest you.</strong></div>
  </section>

  <section class="panel packages">
    <div class="site-url">www.calmiverahealth.example</div>
    <div class="section">
      <h2>Packages</h2>
      <p>Our packages combine favourite treatments at a better price. Choose one for yourself or give it as a gift to someone special.</p>
    </div>
    <div class="special-band">SPECIAL PACKAGES</div>
    <div class="package">
      <h3>Small Package #1</h3>
      <ul>
        <li><svg class="tick" viewBox="0 0 10 10"><path d="M1 5l3 3 5-7" fill="none" stroke="var(--lime-dark)" stroke-width="2"/></svg>60 min relaxation massage</li>
        <li><svg class="tick" viewBox="0 0 10 10"><path d="M1 5l3 3 5-7" fill="none" stroke="var(--lime-dark)" stroke-width="2"/></svg>Express facial</li>
      </ul>
      <div class="price">$75</div>
    </div>
    <div class="package">
      <h3>Small Package #2</h3>
      <ul>
        <li><svg class="tick" viewBox="0 0 10 10"><path d="M1 5l3 3 5-7" fill="none" stroke="var(--lime-dark)" stroke-width="2"/></svg>60 min hot stone massage</li>
        <li><svg class="tick" viewBox="0 0 10 10"><path d="M1 5l3 3 5-7" fill="none" stroke="var(--lime-dark)" stroke-width="2"/></svg>Foot soak and scrub</li>
      </ul>
      <div class="price">$89</div>
    </div>
    <div class="package">
      <h3>Large Package #1</h3>
      <ul>
        <li><svg class="tick" viewBox="0 0 10 10"><path d="M1 5l3 3 5-7" fill="none" stroke="var(--lime-dark)" stroke-width="2"/></svg>90 min deep tissue massage</li>
        <li><svg class="tick" viewBox="0 0 10 10"><path d="M1 5l3 3 5-7" fill="none" stroke="var(--lime-dark)" stroke-width="2"/></svg>Signature facial</li>
        <li><svg class="tick" viewBox="0 0 10 10"><path d="M1 5l3 3 5-7" fill="none" stroke="var(--lime-dark)" stroke-width="2"/></svg>Manicure</li>
      </ul>
      <div class="price">$118</div>
    </div>
    <div class="photo photo-woman" role="img" aria-label="Photo of a woman relaxing at the spa with a flower in her hair"></div>
  </section>
</div>
</body>
</html>
```